Job Recruiting Agemcy

almost like my current site www.qulvex.com but with these changes see and what i meant about the across the to the site says home job companies categories pages blog and login sign up that should only be the 4 i said only 1 home 2 industries 3 jobs 4 contact us. and remove latest blog post and our partners because that's not us we have to post acuarte information thanks and the name of the company if your using is is work and premier staffing solutions and want it easy for us to post and remove jobs and where it emails us every resume or person that applies

Requirements
Must have
• must send email to us when an application is submitted and try to incorparate the colors of current site
Nice to have
• i want a pretty basic site for now just like the one i have but with all thats above were its easy for me being the own to be able to post jobs and everything

```html
<!DOCTYPE html>
<html lang="en">
<head>
<meta charset="utf-8">
<title>Qulvex — Find your job better and faster</title>
<link href="https://fonts.googleapis.com/css2?family=Poppins:wght@400;500;600;700&family=Open+Sans:wght@400;600&display=swap" rel="stylesheet">
<style>
:root{
  --green:#3b8a5c;
  --green-dark:#2f7a4e;
  --green-soft:#e7f3ec;
  --blue:#2aa6d6;
  --blue-light:#4fc0e8;
  --navy:#1d2b4c;
  --text:#5b6478;
  --muted:#9aa2b1;
  --card:#ffffff;
  --line:#e6e9ef;
  --star:#f5a623;
  --tag-orange:#fde3cf;
  --tag-blue:#d8eef9;
  --tag-green:#dcefe3;
}
*{box-sizing:border-box;margin:0;padding:0}
html,body{width:1200px;height:3984px;overflow:hidden}
body{position:relative;background:#fff;font-family:"Open Sans",sans-serif;color:var(--text)}
h1,h2,h3,.brand,.btn,.nav a{font-family:"Poppins",sans-serif}
.deco{position:absolute;left:0;top:0;pointer-events:none}

/* header */
.brand{position:absolute;left:176px;top:24px;display:flex;align-items:center;gap:10px;color:var(--navy);font-weight:700;font-size:26px}
.brand-mark{width:22px;height:22px;border-radius:50%;background:var(--green)}
.brand-tag{position:absolute;left:176px;top:62px;font-size:9px;color:var(--green);font-weight:600;text-transform:lowercase}
.nav{position:absolute;left:646px;top:41px;display:flex;gap:18px;z-index:3}
.nav a{color:#fff;text-decoration:none;font-size:11px;font-weight:500;letter-spacing:.4px;white-space:nowrap}
.btn-login{position:absolute;left:912px;top:28px;width:128px;height:38px;border:1.5px solid #fff;border-radius:4px;color:#fff;font-size:11px;font-weight:500;display:flex;align-items:center;justify-content:center;letter-spacing:.4px;white-space:nowrap;z-index:3}

/* hero */
.hero-title{position:absolute;left:160px;top:232px;font-size:44px;line-height:54px;font-weight:600;color:var(--navy)}
.hero-sub{position:absolute;left:160px;top:344px;font-size:18px;font-weight:500;color:var(--navy);font-family:"Poppins",sans-serif}
.search{position:absolute;left:160px;top:410px;width:400px;height:50px;border-radius:25px;background:#fff;box-shadow:0 6px 20px rgba(29,43,76,.12);display:flex;align-items:center;padding:0 8px 0 24px;font-size:13px;color:var(--muted)}
.search span{flex:1}
.search-btn{width:36px;height:36px;border-radius:50%;background:var(--blue);display:flex;align-items:center;justify-content:center}
.hero-photo{position:absolute;left:622px;top:100px;width:480px;height:480px;border-radius:50%;background:linear-gradient(135deg,#c9d6d8,#6f8b8f 55%,#2f3d40);border:10px solid #fff}

/* about */
.about-photo{position:absolute;left:160px;top:716px;width:424px;height:384px;border-radius:14px;background:linear-gradient(140deg,#d9cfc4,#8a7a6b 50%,#3f3a36)}
.about-title{position:absolute;left:640px;top:824px;font-size:34px;line-height:42px;font-weight:600;color:var(--navy)}
.about-text{position:absolute;left:640px;top:928px;width:400px;font-size:13px;line-height:21px;color:var(--muted)}

/* section titles */
.sec-title{position:absolute;left:0;width:1200px;text-align:center;font-size:34px;font-weight:600;color:var(--navy)}
.sec-sub{position:absolute;left:0;width:1200px;text-align:center;font-size:14px;color:var(--muted)}

/* industries */
.industry{position:absolute;top:1390px;width:236px;height:230px;border-radius:12px;background:var(--card);box-shadow:0 8px 28px rgba(29,43,76,.09);text-align:center;padding-top:56px}
.industry h3{font-size:16px;font-weight:500;color:var(--blue);margin-top:14px}
.industry p{font-size:11px;color:var(--muted);margin-top:4px}
.industry.active{top:1384px;height:242px;background:linear-gradient(160deg,var(--blue-light),var(--blue));padding-top:62px}
.industry.active h3,.industry.active p{color:#fff}
.dots{position:absolute;left:0;width:1200px;display:flex;justify-content:center;gap:10px}
.dots i{width:11px;height:11px;border-radius:50%;background:#c9e7f4}
.dots i.on{background:var(--blue)}

/* jobs */
.jobs-title{position:absolute;left:160px;top:1806px;font-size:34px;font-weight:600;color:var(--navy)}
.btn-all{position:absolute;left:878px;top:1806px;width:162px;height:42px;background:var(--green);color:#fff;border-radius:4px;font-size:11px;font-weight:500;display:flex;align-items:center;justify-content:center;letter-spacing:.5px}
.job{position:absolute;width:272px;height:240px;background:var(--card);border-radius:10px;box-shadow:0 8px 28px rgba(29,43,76,.09);padding:28px 24px}
.job-head{display:flex;align-items:center;gap:10px;font-size:11px;color:var(--muted);white-space:nowrap}
.job-head b{color:var(--navy);font-weight:600}
.job-letter{width:44px;height:44px;border-radius:4px;background:var(--blue);color:#fff;font:600 20px "Poppins",sans-serif;display:flex;align-items:center;justify-content:center;flex:none}
.job h3{font-size:18px;line-height:24px;font-weight:600;color:var(--navy);margin-top:22px;height:52px;display:flex;align-items:center}
.job-meta{font-size:10px;color:var(--muted);margin-top:14px}
.tag{display:inline-block;margin-top:12px;padding:4px 12px;border-radius:3px;font-size:10px;color:var(--navy)}
.tag.orange{background:var(--tag-orange)}
.tag.blue{background:var(--tag-blue)}
.tag.green{background:var(--tag-green)}

/* cta */
.cta{position:absolute;left:160px;top:2578px;width:880px;height:238px;border-radius:10px;background:linear-gradient(120deg,var(--blue-light),var(--blue));text-align:center;color:#fff;padding-top:48px}
.cta h2{font-size:38px;font-weight:500}
.cta p{font-size:13px;margin-top:6px;opacity:.9}
.cta-btns{display:flex;justify-content:center;gap:30px;margin-top:28px}
.cta-btns span{width:140px;height:40px;border:1.5px solid #fff;border-radius:4px;font:500 11px "Poppins",sans-serif;display:flex;align-items:center;justify-content:center}

/* testimonials */
.quote{position:absolute;top:3040px;width:240px;height:284px;background:var(--card);border-radius:10px;box-shadow:0 8px 28px rgba(29,43,76,.09);text-align:center;padding:66px 22px 0}
.avatar{position:absolute;top:2990px;width:84px;height:84px;border-radius:50%;border:5px solid #fff;box-shadow:0 4px 14px rgba(29,43,76,.12)}
.stars{color:var(--star);font-size:17px;letter-spacing:3px}
.stars .off{color:#d7dbe2}
.quote p{font-size:11px;line-height:17px;color:var(--text);margin-top:12px}
.quote .who{font-size:11px;line-height:16px;color:var(--navy);font-weight:600;margin-top:16px}

/* footer */
.footer-title{position:absolute;left:220px;top:3698px;font-size:34px;font-weight:500;color:#fff;font-family:"Poppins",sans-serif}
.subscribe{position:absolute;left:668px;top:3698px;display:flex}
.subscribe .field{width:180px;height:46px;background:#fff;border-radius:3px 0 0 3px;font-size:11px;color:var(--muted);display:flex;align-items:center;padding-left:16px}
.subscribe .go{width:100px;height:46px;background:var(--green-dark);color:#fff;font:500 11px "Poppins",sans-serif;display:flex;align-items:center;justify-content:center;border-radius:0 3px 3px 0;letter-spacing:.5px}
.foot-links{position:absolute;left:220px;top:3840px;display:flex;gap:14px;font-size:12px;color:#fff}
.copy{position:absolute;left:220px;top:3868px;font-size:12px;color:#fff;opacity:.9}
.social{position:absolute;left:820px;top:3842px;display:flex;gap:16px}
.social i{width:32px;height:32px;border-radius:50%;border:1.5px solid #fff}
</style>
</head>
<body>

<svg class="deco" width="1200" height="3984" viewBox="0 0 1200 3984" aria-hidden="true">
  <path d="M560 0 H1200 V560 C1130 620 1020 560 990 470 C960 380 900 330 800 320 C690 310 610 240 600 150 C592 80 575 30 560 0Z" fill="var(--green)"/>
  <path d="M0 470 C60 500 120 560 130 640 C140 720 90 770 0 790Z" fill="var(--green)"/>
  <path d="M0 520 C40 560 70 610 70 660" fill="none" stroke="var(--green-soft)" stroke-width="3"/>
  <path d="M1200 2470 C1120 2500 1090 2580 1120 2650 C1140 2700 1180 2720 1200 2720Z" fill="var(--green)"/>
  <path d="M0 2820 C50 2850 70 2910 40 2960 C25 2985 10 2995 0 3000Z" fill="var(--green)"/>
  <path d="M0 3470 C200 3430 380 3520 560 3520 C760 3520 900 3440 1200 3480 V3984 H0Z" fill="var(--green)"/>
  <path d="M0 3500 C220 3470 390 3560 580 3555 C780 3550 920 3470 1200 3510" fill="none" stroke="#5aa57a" stroke-width="3"/>
  <path d="M1200 3700 C1130 3760 1120 3900 1200 3984Z" fill="var(--green-dark)"/>
</svg>

<div class="brand"><span class="brand-mark"></span>Qulvex</div>
<div class="brand-tag">work and premier staffing solutions</div>
<nav class="nav"><a>HOME</a><a>INDUSTRIES</a><a>JOBS</a><a>CONTACT</a></nav>
<div class="btn-login btn">LOGIN / SIGN UP</div>

<h1 class="hero-title">Find your job<br>better and faster</h1>
<div class="hero-sub">Your career starts here!</div>
<div class="search"><span>Search by skill, company and job</span>
  <div class="search-btn"><svg width="16" height="16" viewBox="0 0 16 16"><circle cx="7" cy="7" r="5" fill="none" stroke="#fff" stroke-width="2"/><path d="M11 11 L14.5 14.5" stroke="#fff" stroke-width="2" stroke-linecap="round"/></svg></div>
</div>
<div class="hero-photo" role="img" aria-label="Photo of a person working at a computer in a bright office"></div>

<div class="about-photo" role="img" aria-label="Photo of two women looking at a laptop together"></div>
<h2 class="about-title">Find Millions of jobs<br>and achieve success</h2>
<p class="about-text">We have over 25 years of specialized recruiting and staffing experience. We cover a broad spectrum of industries to match many of the top aerospace and pharmaceutical commercial employers of today.</p>

<h2 class="sec-title" style="top:1244px">Industries we support</h2>
<p class="sec-sub" style="top:1302px">Choose from the list of most popular categories</p>

<div class="industry" style="left:180px">
  <svg width="64" height="60" viewBox="0 0 64 60" fill="none" stroke="var(--blue)" stroke-width="2.2" stroke-linejoin="round"><path d="M6 34 L58 14 L50 30 L20 40 Z"/><path d="M26 30 L18 18 L24 16 L36 26"/><path d="M10 52 H54"/></svg>
  <h3>Aero Space</h3><p>2 open positions</p>
</div>
<div class="industry active" style="left:482px">
  <svg width="64" height="60" viewBox="0 0 64 60" fill="none" stroke="#fff" stroke-width="2.2" stroke-linejoin="round"><path d="M24 6 H40 M28 6 V22 L14 50 H50 L36 22 V6"/><path d="M20 38 H44"/></svg>
  <h3>Pharmaceutical</h3><p>5 open positions</p>
</div>
<div class="industry" style="left:784px">
  <svg width="64" height="60" viewBox="0 0 64 60" fill="none" stroke="var(--blue)" stroke-width="2.2" stroke-linejoin="round"><path d="M4 16 H38 V42 H4 Z"/><path d="M38 24 H50 L58 33 V42 H38"/><circle cx="14" cy="45" r="5"/><circle cx="48" cy="45" r="5"/></svg>
  <h3>Transportation</h3><p>10 open positions</p>
</div>
<div class="dots" style="top:1674px"><i class="on"></i><i></i><i></i></div>

<h2 class="jobs-title">Hot &amp; Featured Jobs</h2>
<div class="btn-all btn">VIEW ALL JOBS</div>

<div class="job" style="left:160px;top:1900px">
  <div class="job-head"><span class="job-letter">D</span><span><b>Dorvan Inc.</b> 2 days ago</span></div>
  <h3>Aerospace/Aeronautical Engineer</h3>
  <div class="job-meta">Full time in Stratford, CT, USA</div>
  <span class="tag orange">Aero space</span>
</div>
<div class="job" style="left:464px;top:1900px">
  <div class="job-head"><span class="job-letter">E</span><span><b>Elmcrest Freight</b> 2 days ago</span></div>
  <h3>Truck Driver</h3>
  <div class="job-meta">Full time in Chicago, IL, USA</div>
  <span class="tag orange">Transportation</span>
</div>
<div class="job" style="left:768px;top:1900px">
  <div class="job-head"><span class="job-letter">D</span><span><b>Daltrex Co.</b> 3 days ago</span></div>
  <h3>Independent Sales Representative</h3>
  <div class="job-meta">Full time in San Diego, CA, USA</div>
  <span class="tag blue">Pharmaceutical</span>
</div>
<div class="job" style="left:160px;top:2188px">
  <div class="job-head"><span class="job-letter">B</span><span><b>Brixen Health</b> 3 days ago</span></div>
  <h3>Family Physician</h3>
  <div class="job-meta">Full time in Norwalk, NY, USA</div>
  <span class="tag green">Medical</span>
</div>
<div class="job" style="left:464px;top:2188px">
  <div class="job-head"><span class="job-letter">H</span><span><b>Halvern</b> 4 days ago</span></div>
  <h3>Aeronautical Engineer</h3>
  <div class="job-meta">Full time in Stratford, CT, USA</div>
  <span class="tag orange">Aero space</span>
</div>
<div class="job" style="left:768px;top:2188px">
  <div class="job-head"><span class="job-letter">H</span><span><b>Hollis Care</b> 5 days ago</span></div>
  <h3>Healthcare Professional</h3>
  <div class="job-meta">Full time in Stratford, CT, USA</div>
  <span class="tag blue">Medical</span>
</div>

<section class="cta">
  <h2>Seeking For a Job?</h2>
  <p>Discover hundreds of job offers and find the best suitable position</p>
  <div class="cta-btns"><span>SEARCH JOBS</span><span>CREATE AN ACCOUNT</span></div>
</section>

<h2 class="sec-title" style="top:2900px">Testimonials</h2>

<div class="quote" style="left:190px">
  <div class="stars">★★★★★</div>
  <p>"I didn't even need training. I couldn't have asked for more than this. It really saves me time and effort. It is exactly what our business has been lacking."</p>
  <div class="who">Nora Elwin, Senior Account<br>Manager at Brightlane Inc.</div>
</div>
<div class="avatar" style="left:268px;background:linear-gradient(135deg,#e6d3c4,#a98a74)" role="img" aria-label="Portrait of Nora Elwin"></div>

<div class="quote" style="left:480px">
  <div class="stars">★★★★★</div>
  <p>"I was highly impressed by the professionalism shown during my interview process. It was not an interview but more of a conversation with the recruiter."</p>
  <div class="who">Mara Delton, HR Manager<br>at Orchard Labs</div>
</div>
<div class="avatar" style="left:558px;background:linear-gradient(135deg,#d8dde4,#8794a6)" role="img" aria-label="Portrait of Mara Delton"></div>

<div class="quote" style="left:770px">
  <div class="stars">★★★<span class="off">★★</span></div>
  <p>"Thanks for the great service. They have completely surpassed our expectations. This was the most reliable business decision we have ever purchased."</p>
  <div class="who">Ivy Marsh, Brand Manager<br>at Tradewell Inc.</div>
</div>
<div class="avatar" style="left:848px;background:linear-gradient(135deg,#efd9c2,#b7906a)" role="img" aria-label="Portrait of Ivy Marsh"></div>

<div class="dots" style="top:3362px"><i class="on"></i><i></i><i></i></div>

<div class="footer-title">Get started now</div>
<div class="subscribe"><div class="field">Email address</div><div class="go">SUBMIT</div></div>
<div class="foot-links"><span>Privacy Policy</span><span>|</span><span>Terms of Use</span><span>|</span><span>Contact</span><span>|</span><span>Sitemap</span></div>
<div class="copy">© 2020 www.qulvex.com. All rights reserved</div>
<div class="social"><i></i><i></i><i></i></div>

</body>
</html>
```